Modify mobile web Photoshop design to make them look great

We need to choose and refine the stock image to look great on 5 mobile web pages: 1) Hourglass image on home screen, 2) Sofa image on registration screen, 3) Loveseat image on login screen, 4) Lamp for reminder screen, and 5) Bed for ratings / score screen. Sample photos denote what customer wants, but they are just downloaded from Brindo, and is not purchased stock photos. Designers need to show that the updated photos used are properly purchased from stock photo source. Photoshop files for all 5 mobile web pages are provided. Artists are requested to edit and submit the 5 photoshop files and make them look as good as possible with the constraints above. No change is needed on the layout or anything beside the 5 stock images, but subtle refinements are OK if you believe it would improve the overall design without affecting the art direction.

Target Market(s)

Travel, Lifestyle

Industry/Entity Type

Hospitality

Font styles to use
Sans Serif

Requirements
Must have
• Stock photos must be properly licensed, artists must put updated stock photos back into supplied photoshop source files, updated look and feel should have the same general art direction, images must be hourglass, sofa, loveseat, lamp and bed
Nice to have
• Minor and very subtle touchup of other elements without affecting any design work of the layout such as color scheme
Should not have
• Should not affect art direction, identity and color of all design and layout elements, should not use stock image other than the types specified (hourglass, sofa, loveseat, lamp and bed), should not use images not licensed from stock photo sites

```html
<!DOCTYPE html>
<html lang="en">
<head>
<meta charset="utf-8">
<title>Lodgia – Register</title>
<link rel="stylesheet" href="https://fonts.googleapis.com/css2?family=Open+Sans:wght@400;600&family=Nunito:wght@800&display=swap">
<style>
  :root {
    --bg: #6c6c6c;
    --screen: #ffffff;
    --ink: #2b2b2b;
    --purple: #a97bd6;
    --teal: #16948f;
    --magenta: #a3127a;
    --peach: #f0b182;
    --field: #ffffff;
    --panel: rgba(255, 255, 255, 0.38);
    --panel-edge: rgba(255, 255, 255, 0.7);
  }
  * { box-sizing: border-box; margin: 0; padding: 0; }
  html, body { width: 1200px; height: 1200px; overflow: hidden; }
  body {
    background: var(--bg);
    font-family: "Open Sans", sans-serif;
    position: relative;
  }
  .screen {
    position: absolute;
    left: 290px; top: 50px;
    width: 620px; height: 1100px;
    background: var(--screen);
    overflow: hidden;
  }
  .app-header {
    position: absolute; left: 0; top: 0;
    width: 620px; height: 90px;
  }
  .back-button { position: absolute; left: 36px; top: 26px; }
  .menu-button { position: absolute; left: 552px; top: 33px; }
  .brand-name {
    position: absolute; left: 0; right: 0; top: 16px;
    text-align: center;
    font-family: "Nunito", sans-serif;
    font-weight: 800;
    font-size: 48px;
    color: var(--purple);
    letter-spacing: -1px;
  }
  .hero-photo {
    position: absolute; left: 0; top: 90px;
    width: 620px; height: 898px;
    background:
      linear-gradient(90deg, rgba(255,255,255,0.35) 0%, rgba(255,255,255,0) 22%),
      linear-gradient(180deg, #cfc7c1 0%, #ddd6d0 30%, #d9d0c6 55%, #cdbfb0 72%, #c49a6a 86%, #d48a3e 100%);
  }
  .register-panel {
    position: absolute; left: 27px; top: 137px;
    width: 568px; height: 514px;
    background: var(--panel);
    border: 1px solid var(--panel-edge);
    border-radius: 6px;
  }
  .form-field {
    position: absolute; left: 50px;
    width: 464px; height: 44px;
    background: var(--field);
    border-bottom: 2px solid var(--accent);
    display: flex; align-items: center;
  }
  .field-icon {
    width: 52px; height: 100%;
    display: flex; align-items: center; justify-content: center;
    border-right: 1px solid #d7d7d7;
    margin: 8px 0; height: 28px;
  }
  .field-label {
    padding-left: 11px;
    font-size: 17px;
    color: var(--ink);
    flex: 1;
  }
  .dob-tag { font-size: 14px; color: var(--magenta); }
  .calendar-icon { margin-right: 10px; }
  .register-button {
    position: absolute; left: 50px; top: 437px;
    width: 464px; height: 44px;
    background: var(--peach);
    border: none; border-radius: 3px;
    color: #ffffff;
    font-family: "Open Sans", sans-serif;
    font-size: 19px;
    letter-spacing: -0.3px;
  }
  .page-dots {
    position: absolute; left: 0; right: 0; top: 1003px;
    display: flex; justify-content: center; gap: 12px;
  }
  .dot { width: 18px; height: 18px; border-radius: 50%; }
</style>
</head>
<body>
  <main class="screen">
    <header class="app-header">
      <svg class="back-button" width="24" height="38" viewBox="0 0 24 38"><path d="M20 4 L5 19 L20 34" fill="none" stroke="#111" stroke-width="4"/></svg>
      <div class="brand-name">Lodgia</div>
      <svg class="menu-button" width="32" height="20" viewBox="0 0 32 20"><path d="M0 2H32M0 10H32M0 18H32" stroke="#222" stroke-width="2"/></svg>
    </header>

    <div class="hero-photo" role="img" aria-label="Bright living room with a beige sectional sofa beside a window with blinds and a wooden floor"></div>

    <form class="register-panel">
      <div class="form-field" style="top:43px; --accent: var(--purple);">
        <span class="field-icon"><svg width="22" height="24" viewBox="0 0 22 24" fill="none" stroke="var(--purple)" stroke-width="1.5"><circle cx="11" cy="7" r="5"/><path d="M2 23c0-6 4-9 9-9s9 3 9 9z"/></svg></span>
        <span class="field-label">Full Name</span>
      </div>
      <div class="form-field" style="top:108px; --accent: var(--teal);">
        <span class="field-icon"><svg width="30" height="20" viewBox="0 0 30 20" fill="none" stroke="var(--teal)" stroke-width="1.5"><rect x="1" y="1" width="28" height="18"/><circle cx="9" cy="8" r="3"/><path d="M4 16c0-4 10-4 10 0M17 7h9M17 11h9M17 15h6"/></svg></span>
        <span class="field-label">ID Number</span>
      </div>
      <div class="form-field" style="top:173px; --accent: var(--magenta);">
        <span class="field-icon"><span class="dob-tag">DOB</span></span>
        <span class="field-label">06/09/1980</span>
        <svg class="calendar-icon" width="26" height="26" viewBox="0 0 26 26" fill="none" stroke="var(--magenta)" stroke-width="2"><rect x="2" y="5" width="22" height="19" rx="2"/><path d="M2 10h22M8 2v6M18 2v6"/><path d="M7 14h2M12 14h2M17 14h2M7 19h2M12 19h2M17 19h2" stroke-width="2.5"/></svg>
      </div>
      <div class="form-field" style="top:238px; --accent: var(--peach);">
        <span class="field-icon"><svg width="16" height="26" viewBox="0 0 16 26"><rect x="1" y="1" width="14" height="24" rx="2" fill="none" stroke="var(--peach)" stroke-width="1.5"/><rect x="3" y="4" width="10" height="15" fill="var(--peach)"/><circle cx="8" cy="22" r="1.2" fill="var(--peach)"/></svg></span>
        <span class="field-label">Mobile Number</span>
      </div>
      <div class="form-field" style="top:303px; --accent: var(--teal);">
        <span class="field-icon"><svg width="22" height="22" viewBox="0 0 22 22"><circle cx="15" cy="7" r="6" fill="var(--teal)"/><path d="M11 11 L2 20 M4 18 L7 21" stroke="var(--teal)" stroke-width="3" fill="none"/></svg></span>
        <span class="field-label">Set Password</span>
      </div>
      <div class="form-field" style="top:368px; --accent: var(--purple);">
        <span class="field-icon"><svg width="22" height="16" viewBox="0 0 22 16"><rect x="0" y="0" width="22" height="16" fill="var(--purple)"/><path d="M1 1 L11 9 L21 1 M1 15 L8 8 M21 15 L14 8" stroke="#fff" stroke-width="1.3" fill="none"/></svg></span>
        <span class="field-label">Email</span>
      </div>
      <button class="register-button" type="button">REGISTER NOW</button>
    </form>

    <nav class="page-dots">
      <span class="dot" style="background:var(--purple)"></span>
      <span class="dot" style="background:var(--teal)"></span>
      <span class="dot" style="background:var(--magenta)"></span>
      <span class="dot" style="background:var(--peach)"></span>
      <span class="dot" style="background:var(--teal)"></span>
    </nav>
  </main>
</body>
</html>
```